Pull Up Banners

Would like to have these pull up banner designs changed to a new modern theme. I have running a sales booth and want to re-design the banner designs. I have uploaded old banner design, I need phone number and website added onto bottom. Happy to consider images to attract people attention to increase sales and spark people interest walking past.

```html
<!DOCTYPE html>
<html lang="en">
<head>
<meta charset="utf-8">
<title>Nexora Pull Up Banners</title>
<link href="https://fonts.googleapis.com/css2?family=Poppins:wght@500;600;700;800&family=Exo+2:wght@700&display=swap" rel="stylesheet">
<style>
  :root{
    --orange:#ec5a14;
    --orange-deep:#d94a0b;
    --ink:#1d1d1f;
    --black:#0d0d0d;
    --white:#ffffff;
    --panel:#f3f3f4;
    --panel-deep:#e4e4e6;
    --stage:#eeeeef;
  }
  *{margin:0;padding:0;box-sizing:border-box}
  html,body{width:1200px;height:1159px;overflow:hidden}
  body{background:var(--stage);font-family:"Poppins",sans-serif;color:var(--ink);position:relative}

  .banner{position:absolute;top:140px;width:360px;height:880px;background:var(--white);overflow:hidden;box-shadow:0 6px 24px rgba(0,0,0,.12)}
  .banner--phone{left:195px}
  .banner--managed{left:648px}

  .brand{position:absolute;top:0;left:0;right:0;height:95px;display:flex;align-items:center;justify-content:center;gap:12px}
  .brand__dot{width:34px;height:34px;border-radius:50%;background:var(--orange)}
  .brand__text{display:flex;flex-direction:column}
  .brand__name{font-weight:600;font-size:27px;letter-spacing:4px;color:var(--orange);line-height:1}
  .brand__tag{font-weight:600;font-size:5.6px;letter-spacing:1.3px;color:var(--ink);margin-top:3px}

  .hero{position:absolute;top:95px;left:0;right:0;height:367px}
  .hero--cloud{background:radial-gradient(circle at 55% 42%,#7fe3ff 0%,#2a9fd0 18%,#0f4f78 45%,#0a2238 80%)}
  .hero--team{background:linear-gradient(100deg,#3a4250 0%,#5a6b86 40%,#2f5ea0 70%,#9ec0ea 100%)}

  .title-band{position:absolute;top:462px;left:0;right:0;height:99px;background:linear-gradient(90deg,var(--orange-deep),var(--orange) 50%,var(--orange-deep));display:flex;align-items:center;justify-content:center;text-align:center;color:var(--white);font-weight:700;text-transform:uppercase}
  .title-band::after{content:"";position:absolute;left:50%;bottom:-11px;margin-left:-12px;border-left:12px solid transparent;border-right:12px solid transparent;border-top:12px solid var(--orange-deep)}
  .title-band--phone{font-size:28.5px;line-height:33px}
  .title-band--managed{font-size:36px;line-height:38px;font-weight:800}

  .services{position:absolute;top:561px;left:0;right:0;height:250px;background:linear-gradient(180deg,var(--white) 0%,var(--panel) 50%,var(--panel-deep) 100%)}
  .services__divider{position:absolute;left:179px;top:28px;height:184px;width:1px;background:#c9c9cc}
  .service{position:absolute;width:150px;margin-left:-75px;text-align:center;font-weight:600;color:var(--ink)}
  .service__icon{width:52px;height:52px;margin:0 auto 8px;border-radius:50%;border:3px solid var(--ink);border-top-color:var(--orange);background:var(--white);display:flex;align-items:center;justify-content:center;box-shadow:0 2px 4px rgba(0,0,0,.15)}
  .service__icon svg{width:28px;height:28px}
  .banner--phone .service{font-size:14px;line-height:18px}
  .banner--managed .service{font-size:12px;line-height:16px;width:110px;margin-left:-55px}

  .footer{position:absolute;left:0;right:0;bottom:0;height:69px;background:var(--black)}
  .call{position:absolute;top:792px;left:50%;width:286px;margin-left:-143px;height:40px;background:var(--orange);clip-path:polygon(6% 0,94% 0,100% 50%,94% 100%,6% 100%,0 50%);display:flex;align-items:center;justify-content:center;gap:8px;color:var(--white);font-family:"Exo 2",sans-serif;font-weight:700;font-size:34px;letter-spacing:1px}
  .call svg{width:24px;height:24px}
  .web{position:absolute;left:0;right:0;bottom:14px;text-align:center;color:var(--white);font-size:17px;font-weight:500}
  .web span{color:var(--orange)}
</style>
</head>
<body>

<svg width="0" height="0" style="position:absolute" aria-hidden="true">
  <defs>
    <symbol id="i-phone" viewBox="0 0 24 24"><path fill="#ec5a14" d="M6.6 10.8a15 15 0 006.6 6.6l2.2-2.2c.3-.3.7-.4 1-.2 1.1.4 2.3.6 3.6.6.6 0 1 .4 1 1V20c0 .6-.4 1-1 1A17 17 0 013 4c0-.6.4-1 1-1h3.5c.6 0 1 .4 1 1 0 1.3.2 2.5.6 3.6.1.3 0 .7-.2 1z"/></symbol>
    <symbol id="i-chat" viewBox="0 0 24 24"><path fill="#ec5a14" d="M3 4h18v12H9l-4 4v-4H3z"/><path stroke="#fff" stroke-width="1.6" d="M7 8h10M7 11h10M7 14h6"/></symbol>
    <symbol id="i-people" viewBox="0 0 24 24"><g fill="#ec5a14"><circle cx="12" cy="7" r="3"/><circle cx="5" cy="9" r="2.3"/><circle cx="19" cy="9" r="2.3"/><path d="M6.5 19c0-4 2.5-6.5 5.5-6.5s5.5 2.5 5.5 6.5z"/><path d="M1 19c0-3 1.7-5 4-5 1 0 1.7.3 2.3.8A8 8 0 005.5 19zM23 19c0-3-1.7-5-4-5-1 0-1.7.3-2.3.8a8 8 0 011.8 4.2z"/></g></symbol>
    <symbol id="i-wifi" viewBox="0 0 24 24"><g fill="none" stroke="#ec5a14" stroke-width="2.4" stroke-linecap="round"><path d="M2 9a15 15 0 0120 0"/><path d="M5.5 12.5a10 10 0 0113 0"/><path d="M9 16a5 5 0 016 0"/></g><circle cx="12" cy="19.5" r="1.8" fill="#ec5a14"/></symbol>
    <symbol id="i-monitor" viewBox="0 0 24 24"><rect x="2" y="3" width="20" height="13" rx="1.5" fill="none" stroke="#ec5a14" stroke-width="2"/><path fill="#ec5a14" d="M9 17h6l1 3H8z"/><rect x="6" y="20" width="12" height="1.6" fill="#ec5a14"/></symbol>
    <symbol id="i-shield" viewBox="0 0 24 24"><path fill="none" stroke="#ec5a14" stroke-width="2" d="M12 2l8 3v6c0 5-3.5 9-8 11-4.5-2-8-6-8-11V5z"/><rect x="9" y="11" width="6" height="5" fill="#ec5a14"/><path fill="none" stroke="#ec5a14" stroke-width="1.6" d="M10 11V9.5a2 2 0 014 0V11"/></symbol>
    <symbol id="i-cloud" viewBox="0 0 24 24"><path fill="none" stroke="#ec5a14" stroke-width="1.8" d="M7 14a4 4 0 01-.5-8A5.5 5.5 0 0117 6.5 3.8 3.8 0 0117.5 14z"/><path stroke="#ec5a14" stroke-width="1.6" d="M12 14v4M7 14v3M17 14v3"/><g fill="#ec5a14"><circle cx="12" cy="19.5" r="1.6"/><circle cx="7" cy="18.5" r="1.6"/><circle cx="17" cy="18.5" r="1.6"/></g></symbol>
    <symbol id="i-mail" viewBox="0 0 24 24"><rect x="2" y="5" width="20" height="14" rx="1.5" fill="#ec5a14"/><path fill="none" stroke="#fff" stroke-width="1.6" d="M3 6.5l9 6.5 9-6.5"/></symbol>
    <symbol id="i-globe" viewBox="0 0 24 24"><g fill="none" stroke="#ec5a14" stroke-width="1.6"><circle cx="12" cy="12" r="9"/><ellipse cx="12" cy="12" rx="4" ry="9"/><path d="M3 12h18M4.5 7.5h15M4.5 16.5h15"/></g></symbol>
    <symbol id="i-call" viewBox="0 0 24 24"><path fill="#fff" d="M6.6 10.8a15 15 0 006.6 6.6l2.2-2.2c.3-.3.7-.4 1-.2 1.1.4 2.3.6 3.6.6.6 0 1 .4 1 1V20c0 .6-.4 1-1 1A17 17 0 013 4c0-.6.4-1 1-1h3.5c.6 0 1 .4 1 1 0 1.3.2 2.5.6 3.6.1.3 0 .7-.2 1z" transform="scale(-1,1) translate(-24,0)"/></symbol>
  </defs>
</svg>

<section class="banner banner--phone">
  <header class="brand">
    <span class="brand__dot"></span>
    <div class="brand__text">
      <span class="brand__name">NEXORA</span>
      <span class="brand__tag">SMART SUPPORT FOR EVERY I.T NEED</span>
    </div>
  </header>
  <div class="hero hero--cloud" role="img" aria-label="Business person holding a glowing digital cloud with upload and download arrows"></div>
  <h2 class="title-band title-band--phone">Cloud Phone<br>System &amp; Internet</h2>
  <div class="services">
    <div class="services__divider"></div>
    <div class="service" style="left:99px;top:15px"><div class="service__icon"><svg><use href="#i-phone"/></svg></div>VoIP &amp; Phone<br>Systems</div>
    <div class="service" style="left:259px;top:15px"><div class="service__icon"><svg><use href="#i-chat"/></svg></div>SMS<br>Gateway</div>
    <div class="service" style="left:99px;top:124px"><div class="service__icon"><svg><use href="#i-people"/></svg></div>Unified<br>Group Calling</div>
    <div class="service" style="left:262px;top:124px"><div class="service__icon"><svg><use href="#i-wifi"/></svg></div>Broadband, Fibre<br>&amp; 4G Internet</div>
  </div>
  <footer class="footer"><p class="web">www.<span>nexoratech</span>.com.au</p></footer>
  <div class="call"><svg><use href="#i-call"/></svg>1300 555 019</div>
</section>

<section class="banner banner--managed">
  <header class="brand">
    <span class="brand__dot"></span>
    <div class="brand__text">
      <span class="brand__name">NEXORA</span>
      <span class="brand__tag">SMART SUPPORT FOR EVERY I.T NEED</span>
    </div>
  </header>
  <div class="hero hero--team" role="img" aria-label="Two IT engineers with a laptop in a server room touching a holographic interface"></div>
  <h2 class="title-band title-band--managed">Managed I.T<br>Services</h2>
  <div class="services">
    <div class="service" style="left:72px;top:25px"><div class="service__icon"><svg><use href="#i-monitor"/></svg></div>Managed<br>I.T Support</div>
    <div class="service" style="left:179px;top:25px"><div class="service__icon"><svg><use href="#i-shield"/></svg></div>Cybersecurity<br>Solutions</div>
    <div class="service" style="left:289px;top:25px"><div class="service__icon"><svg><use href="#i-cloud"/></svg></div>Cloud Servers<br>&amp; Backups</div>
    <div class="service" style="left:125px;top:124px"><div class="service__icon"><svg><use href="#i-mail"/></svg></div>Business<br>Email Packs</div>
    <div class="service" style="left:235px;top:124px"><div class="service__icon"><svg><use href="#i-globe"/></svg></div>Domains &amp;<br>Websites</div>
  </div>
  <footer class="footer"><p class="web">www.<span>nexoratech</span>.com.au</p></footer>
  <div class="call"><svg><use href="#i-call"/></svg>1300 555 019</div>
</section>

</body>
</html>
```